Pharmacy handmade, Personalized Medical Cosmetics Label

Medical Cosmetics label, elegant and professional looking. The creams are Dermatologist formulated and are prepared by local Pharmacy. The label should be versatile and allow space for hand writing to be filled by the pharmacist preparing the product.
The following information will be handwritten:
Upper lid - Eye Care No.3 ; Marigold, Retinol ; 30
Lower Bottom - Teodora Brandt ; Signature ; 01.01.2017
Upper Lid Label
Vella Skin (logo)
Doctor Series
(circular pattern - Doctor Formulated, Registered Pharmacy, Handmade, Highest Medical Standards)
(Eye Care No.3 - in hand writing and different color, maybe red)
Key Ingredients: (Marigold, Retinol - in hand writing, same color as above, maybe red)
(box with hand writing 30) ml
Lower Bottom Label (underneath surface of the container)
Made for Vella Skin by
Pharmacy Estrel, 7 Kalina blvd., Sofia, ph. 0893517640
Patient: (Teodora Brandt- in hand writing)
Pharmacist: (Signature - in hand writing)
Date: (01.01.2017 - in hand writing)
For External Use
good for 60 days after preparation
Ingredients: Retinol, Marigold Extract, Water, Glycerin, Stearyl Alcohol, Wheat Germ Oil, Polysorbate 60, Sesame Oil, Myristyl Myristate, Cetyl Alcohol, Sorbitan Stearate, Phenoxyethanol, Calendula Extract, Cornflower Extract, Sodium Alginate, Sodium Citrate.
The container lid and bottom are 5 cm = 50 mm in diameter. Made from aluminum and contain 30ml or 50ml.
Please refer to the screen shots from my Web Site to get the feeling for the color pallet and professional look. These creams will be sold on this website. They are custom made by a registered Pharmacy right on the spot after the order has been placed. This is why I need more space for the hand written notes made by the pharmacist who prepared the order.
Please make the design professional, simple and serious colors, like light brown, beige, black or dark brown letters, red hand writing (will be filled by pen or thin marker by the Pharmacist by hand, depending on the order, patient name, etc.)
Thank you.
Target Market(s)
female 24 - 49 year old
Industry/Entity Type
Medical

```html
<!DOCTYPE html>
<html lang="en">
<head>
<meta charset="utf-8">
<title>Vella Skin – Doctor Series Labels</title>
<link rel="stylesheet" href="https://fonts.googleapis.com/css2?family=Raleway:wght@400;500&family=Open+Sans:wght@400&family=Caveat:wght@500&display=swap">
<style>
  :root {
    --ring-grey: #d1d2d4;
    --sand: #a39382;
    --cocoa: #7d6b5c;
    --taupe-text: #9a8a7b;
    --label-grey: #8c8c8c;
    --ink: #222222;
    --pen-red: #e0242f;
    --paper: #ffffff;
  }
  html, body {
    margin: 0;
    width: 1138px;
    height: 1200px;
    overflow: hidden;
    background: var(--paper);
  }
  .sheet {
    position: absolute;
    left: 0;
    top: 316px;
    width: 1138px;
    height: 568px;
  }
  .ring { fill: var(--ring-grey); }
  .paper { fill: var(--paper); }
  .cap-light { fill: var(--sand); }
  .cap-dark { fill: var(--cocoa); }
  .edge { fill: none; stroke: var(--taupe-text); stroke-width: 1.5; }
  .brand-disc { fill: none; stroke: var(--paper); stroke-width: 3; }
  .brand-name { font-family: "Raleway", sans-serif; font-weight: 400; font-size: 58px; fill: var(--paper); }
  .series { font-family: "Raleway", sans-serif; font-size: 31px; letter-spacing: 1px; fill: var(--paper); text-anchor: middle; }
  .claims { font-family: "Raleway", sans-serif; font-weight: 500; font-size: 27px; fill: var(--taupe-text); }
  .pen { font-family: "Caveat", cursive; font-weight: 500; fill: var(--pen-red); }
  .heading { font-family: "Raleway", sans-serif; font-size: 23px; fill: var(--paper); text-anchor: middle; }
  .rule-white { stroke: var(--paper); stroke-width: 1.2; }
  .ingredients { font-family: "Raleway", sans-serif; font-size: 17px; fill: var(--paper); text-anchor: middle; }
  .maker { font-family: "Raleway", sans-serif; font-size: 17.5px; fill: var(--paper); text-anchor: middle; }
  .field-label { font-family: "Raleway", sans-serif; font-size: 21px; fill: var(--label-grey); }
  .field-line { stroke: var(--label-grey); stroke-width: 1; }
  .signature { fill: var(--pen-red); opacity: 0.18; }
  .usage-box { fill: none; stroke: var(--label-grey); stroke-width: 1; }
  .usage { font-family: "Raleway", sans-serif; font-size: 13.5px; fill: var(--label-grey); text-anchor: middle; }
  .shelf-life { font-family: "Raleway", sans-serif; font-size: 11.5px; fill: var(--label-grey); text-anchor: middle; }
  .caption { font-family: "Open Sans", sans-serif; font-size: 22px; fill: var(--ink); text-anchor: middle; }
  .pointer { stroke: var(--ink); stroke-width: 1; fill: none; }
  .pointer-dot { fill: var(--ink); }
</style>
</head>
<body>
<svg class="sheet" viewBox="0 0 1422 710" xmlns="http://www.w3.org/2000/svg">
  <defs>
    <clipPath id="lid-face"><circle cx="312" cy="312" r="240"/></clipPath>
    <clipPath id="base-face"><circle cx="312" cy="312" r="266"/></clipPath>
    <path id="claims-track" d="M126.7,126.7 A262,262 0 1,1 497.3,497.3 A262,262 0 1,1 126.7,126.7"/>
  </defs>

  <!-- callout -->
  <text class="caption" x="703" y="48">SURFACE OF THE CONTAINER</text>
  <polyline class="pointer" points="570,138 703,60 828,136"/>
  <circle class="pointer-dot" cx="570" cy="138" r="3.5"/>
  <circle class="pointer-dot" cx="828" cy="136" r="3.5"/>

  <!-- upper lid label -->
  <g class="lid-label" transform="translate(60 30)">
    <circle class="ring" cx="312" cy="312" r="312"/>
    <circle class="paper" cx="312" cy="312" r="290"/>
    <text class="claims"><textPath href="#claims-track" textLength="1620" lengthAdjust="spacing">DOCTOR FORMULATED • REGISTERED PHARMACY • HANDMADE • HIGHEST MEDICAL STANDARDS •</textPath></text>
    <g clip-path="url(#lid-face)">
      <rect class="cap-light" x="0" y="0" width="624" height="283"/>
      <rect class="cap-dark" x="0" y="283" width="624" height="57"/>
      <rect class="paper" x="0" y="340" width="624" height="284"/>
    </g>
    <circle class="edge" cx="312" cy="312" r="242"/>
    <circle class="brand-disc" cx="198" cy="205" r="62"/>
    <text class="brand-name" x="280" y="195">vella</text>
    <text class="brand-name" x="280" y="240">skin</text>
    <text class="series" x="312" y="325">DOCTOR SERIES</text>
    <text class="pen" x="288" y="412" font-size="42" text-anchor="middle">EYE CARE No. 3</text>
    <text class="pen" x="288" y="448" font-size="34" text-anchor="middle">Marigold, Retinol</text>
    <text class="pen" x="288" y="496" font-size="40" text-anchor="middle">30 ml</text>
  </g>
  <text class="caption" x="372" y="704">UPPER LID LABEL</text>

  <!-- lower bottom label -->
  <g class="base-label" transform="translate(730 30)">
    <circle class="ring" cx="312" cy="312" r="312"/>
    <circle class="paper" cx="312" cy="312" r="292"/>
    <g clip-path="url(#base-face)">
      <rect class="cap-light" x="0" y="0" width="624" height="280"/>
      <rect class="cap-dark" x="0" y="280" width="624" height="62"/>
      <rect class="paper" x="0" y="342" width="624" height="282"/>
    </g>
    <circle class="edge" cx="312" cy="312" r="268"/>

    <line class="rule-white" x1="230" y1="84" x2="394" y2="84"/>
    <text class="heading" x="312" y="110">INGREDIENTS</text>
    <line class="rule-white" x1="230" y1="119" x2="394" y2="119"/>
    <text class="ingredients">
      <tspan x="312" y="144">Retinol, Marigold Extract, Water,</tspan>
      <tspan x="312" y="168">Glycerin, Stearyl Alcohol, Wheat Germ Oil,</tspan>
      <tspan x="312" y="191">Polysorbate 60, Sesame Oil, Myristyl Myristate,</tspan>
      <tspan x="312" y="215">Cetyl Alcohol, Sorbitan Stearate, Phenoxyethanol,</tspan>
      <tspan x="312" y="238">Calendula Extract, Cornflower Extract, Sodium</tspan>
      <tspan x="312" y="262">Alginate, Sodium Citrate.</tspan>
    </text>

    <text class="maker" x="312" y="305">MADE FOR VELLA SKIN BY</text>
    <text class="maker" x="312" y="329">Pharmacy Estrel, 7 Kalina blvd., Sofia, ph. 0893517640</text>

    <text class="field-label" x="80" y="387">Patient:</text>
    <line class="field-line" x1="165" y1="388" x2="537" y2="388"/>
    <text class="pen" x="205" y="381" font-size="38">Teodora Brandt</text>

    <text class="field-label" x="113" y="432">Pharmacist:</text>
    <line class="field-line" x1="240" y1="433" x2="505" y2="433"/>
    <rect class="signature" x="282" y="398" width="175" height="32" rx="4" role="img" aria-label="Pharmacist's handwritten signature"/>

    <text class="field-label" x="153" y="476">Date:</text>
    <line class="field-line" x1="215" y1="478" x2="465" y2="478"/>
    <text class="pen" x="250" y="470" font-size="36">07.02.2017</text>

    <rect class="usage-box" x="238" y="502" width="146" height="19"/>
    <text class="usage" x="311" y="516">FOR EXTERNAL USE</text>
    <text class="shelf-life" x="311" y="539">good for 60 days after preparation</text>
  </g>
  <text class="caption" x="1032" y="704">LOWER BOTTOM LABEL</text>
</svg>
</body>
</html>
```